Push notification screens at app start up

We have an existing news publication app platform and are adding categories to push notifications.

We need two screens designed (each for Novaro, Tavlet and Morvelin for a total of 6d) that show when the app is first launched.

The workflow of our app:
0. app launch screen while webservices run (no work needed)
1. information screen to the user promoting the benefits of push notification with "Next" button. (see concept attached)
2. Push categories selection screen. This will have list of category types, with on/off switch.

"Select the categories that you wish to receive occasional notices:
Breaking News (on/off switch)
Local News (on/off switch)
Sports (on/off switch)
Local Events (on/off switch)
Weather Alerts (on/off switch)
Local Deals (on/off switch)"

"Enable these categories on the next screen."
"Next" button

Background:
When I was looking around at app designs, I came across this one (http://www.pixelvane.net/design/7148305) and I really liked it. We obviously have different features on our screen, but I’d like to have this same feel. The colors used in this design are perfect.

UPDATE: I do not mean to limit your design to match the layout as the one mentioned above. Please use your creativity for the layout.

Our standard font in Helvetica Neue.

Notes:
- our app is developed for all phone devices from Novaro 4 to Novaro 6, so designs should be thoughtful of vertical scrolling if needed.
- our app is developed for Tavlets, so we'll need designs completed as well. (We can finalize Novaro design first, then translate the design to Tavlet.)
- our app is developed for Morvelin phones (not tablets), so we'll need designs completed as well. (We can finalize Kvo design first, then translater to Morvelin UI design guidelines).

We hope to establish a good on-going relationship with the designer for as-needed work in the future.

Industry/Entity Type

News

Font styles to use
Other font styles liked:
• Helvetica Neue

Requirements
Must have
• Clean designs. No clutter.
Nice to have
• We would likely go with the standard on/off switches for both Kvo and Morvelin, but are open to small custom variations.

```html
<!DOCTYPE html>
<html lang="en">
<head>
<meta charset="utf-8">
<title>Notifications onboarding screen</title>
<link rel="stylesheet" href="https://fonts.googleapis.com/css2?family=Roboto:wght@300;400&display=swap">
<style>
  :root {
    --status-bg: #0d0d0d;
    --status-text: #ffffff;
    --header-bg: #e3e3e3;
    --screen-bg: #ffffff;
    --accent: #3b9ad9;
    --title: #2b2b2b;
    --body: #3a3a3a;
    --button-text: #ffffff;
  }
  * { box-sizing: border-box; margin: 0; padding: 0; }
  html, body {
    width: 1200px;
    height: 2352px;
    overflow: hidden;
    background: var(--screen-bg);
    font-family: "Roboto", "Helvetica Neue", Arial, sans-serif;
  }
  .screen {
    position: relative;
    width: 1200px;
    height: 2352px;
    background: var(--screen-bg);
    overflow: hidden;
  }
  .status-bar {
    position: relative;
    height: 76px;
    background: var(--status-bg);
    color: var(--status-text);
    display: flex;
    align-items: center;
    justify-content: space-between;
    padding: 0 28px;
    font-size: 34px;
    font-weight: 400;
    z-index: 2;
  }
  .status-left, .status-right { display: flex; align-items: center; gap: 12px; }
  .status-time { position: absolute; left: 0; right: 0; text-align: center; }
  .signal { display: flex; gap: 5px; }
  .signal span { width: 13px; height: 13px; border-radius: 50%; border: 2px solid var(--status-text); }
  .signal span.on { background: var(--status-text); }
  .header-band {
    position: relative;
    height: 205px;
    background: var(--header-bg);
  }
  .bell-badge {
    position: absolute;
    left: 50%;
    top: 14px;
    width: 336px;
    height: 336px;
    margin-left: -168px;
    border-radius: 50%;
    background: var(--header-bg);
  }
  .bell-badge svg {
    position: absolute;
    left: 50%;
    top: 94px;
    width: 136px;
    height: 136px;
    margin-left: -68px;
  }
  .content {
    position: relative;
    padding: 300px 40px 0;
  }
  .title {
    text-align: center;
    font-size: 54px;
    font-weight: 400;
    color: var(--title);
    letter-spacing: 1px;
    margin-bottom: 26px;
  }
  .body-copy {
    font-size: 50px;
    font-weight: 300;
    line-height: 64px;
    color: var(--body);
    text-align: left;
  }
  .body-copy + .body-copy { margin-top: 64px; }
  .next-button {
    position: absolute;
    left: 0;
    bottom: 0;
    width: 1200px;
    height: 150px;
    background: var(--accent);
    color: var(--button-text);
    display: flex;
    align-items: center;
    justify-content: center;
    font-size: 48px;
    font-weight: 300;
    letter-spacing: 2px;
    gap: 22px;
  }
</style>
</head>
<body>
  <main class="screen">
    <div class="status-bar">
      <div class="status-left">
        <div class="signal"><span class="on"></span><span class="on"></span><span class="on"></span><span></span><span></span></div>
        <span>ORBIT</span>
        <svg width="38" height="30" viewBox="0 0 40 32" aria-hidden="true">
          <path d="M4 12 A22 22 0 0 1 36 12" fill="none" stroke="#fff" stroke-width="4"/>
          <path d="M10 18 A14 14 0 0 1 30 18" fill="none" stroke="#fff" stroke-width="4"/>
          <circle cx="20" cy="26" r="4" fill="#fff"/>
        </svg>
      </div>
      <div class="status-time">4:21 PM</div>
      <div class="status-right">
        <span>100%</span>
        <svg width="66" height="30" viewBox="0 0 70 32" aria-hidden="true">
          <rect x="2" y="2" width="60" height="28" rx="4" fill="none" stroke="#fff" stroke-width="3"/>
          <rect x="6" y="6" width="52" height="20" rx="2" fill="#fff"/>
          <rect x="64" y="10" width="4" height="12" fill="#fff"/>
        </svg>
      </div>
    </div>

    <div class="header-band">
      <div class="bell-badge">
        <svg viewBox="0 0 100 100" aria-hidden="true">
          <g fill="none" stroke="var(--accent)" stroke-width="5" stroke-linejoin="round" stroke-linecap="round">
            <circle cx="50" cy="12" r="5"/>
            <path d="M50 17 C32 17 26 30 26 46 V62 L16 76 H84 L74 62 V46 C74 30 68 17 50 17 Z"/>
            <path d="M40 82 A10 10 0 0 0 60 82"/>
          </g>
        </svg>
      </div>
    </div>

    <section class="content">
      <h1 class="title">NOTIFICATIONS</h1>
      <p class="body-copy">By enabling push notifications, you can keep you up to date with occasional notifications related to items you care about. Select the categories on the next screen and then authorize the push noticfcations.</p>
      <p class="body-copy">If you ever change your mind, you can adjust these options in the Settings menu of this app.</p>
    </section>

    <div class="next-button">
      <span>NEXT</span>
      <svg width="20" height="36" viewBox="0 0 22 40" aria-hidden="true">
        <path d="M3 4 L18 20 L3 36" fill="none" stroke="#fff" stroke-width="3"/>
      </svg>
    </div>
  </main>
</body>
</html>
```